Business Card Design Project

Services provide - supply and install all types of curtains - sheer, blackout, shower curtains, wall decor stickers, wall oil paintings
free consultation, unbeatable prices

homed decor industry
Updates

Reason: not happy with designs, smb need to all me to discuss what exactly to change thanks 202-555-0148

Target Market(s)

Maryland

Industry/Entity Type

Business

Contact Information for Business Card

have pictures of 2-3 curtains on business card and logo

Font styles to use
Serif

Colors
b767a9
f68d4c
e34197
fece3e
fbee3e
b768aa
000000
e667a6

Requirements
Must have
• logo, pictures
• slogan "Interiors that Reflect your Style"
• phone number 202-555-0163

```html
<!DOCTYPE html>
<html lang="en">
<head>
<meta charset="utf-8">
<title>Willow Lane Interiors – Business Card</title>
<link href="https://fonts.googleapis.com/css2?family=Questrial&display=swap" rel="stylesheet">
<style>
  :root {
    --stage: #4e1417;
    --sheer-light: #f3eef0;
    --sheer-mid: #ecdde2;
    --sheer-rose: #e9c9d2;
    --frame: rgba(255, 255, 255, 0.55);
    --panel: rgba(255, 255, 255, 0.62);
    --ink: #2f2424;
    --accent: #b3242b;
  }
  * { box-sizing: border-box; margin: 0; padding: 0; }
  html, body { width: 1200px; height: 1000px; overflow: hidden; }
  body {
    background: var(--stage);
    font-family: "Questrial", "Helvetica Neue", Arial, sans-serif;
    color: var(--ink);
    position: relative;
  }
  .card {
    position: absolute;
    left: 262px;
    width: 676px;
    height: 406px;
    overflow: hidden;
    box-shadow: 0 2px 10px rgba(0,0,0,0.35);
  }
  .card--front { top: 82px; }
  .card--back { top: 522px; }
  .sheer-backdrop {
    position: absolute; inset: 0;
    background:
      radial-gradient(ellipse at 70% 40%, var(--sheer-rose) 0%, transparent 60%),
      radial-gradient(ellipse at 20% 80%, var(--sheer-rose) 0%, transparent 55%),
      linear-gradient(90deg, var(--sheer-light), var(--sheer-mid) 45%, var(--sheer-light) 70%, var(--sheer-mid));
  }
  .inner-frame {
    position: absolute;
    left: 18px; top: 14px; right: 18px; bottom: 18px;
    border: 9px solid var(--frame);
  }
  .brand {
    position: absolute;
    left: 38px; top: 150px;
    width: 290px;
  }
  .brand__name {
    display: flex; align-items: center; gap: 12px;
    font-size: 33px;
    line-height: 1.1;
    color: var(--accent);
  }
  .brand__dot {
    width: 16px; height: 16px; border-radius: 50%;
    background: var(--accent); flex: none;
  }
  .brand__tagline {
    margin-top: 10px;
    font-size: 13px;
    color: var(--ink);
  }
  .slogan {
    position: absolute;
    right: 38px; top: 270px;
    width: 200px;
    text-align: center;
    font-size: 24px;
    line-height: 33px;
    color: var(--ink);
  }
  .photo {
    position: absolute;
    top: 20px;
    width: 200px; height: 194px;
    border: 8px solid var(--frame);
  }
  .photo__fill { width: 100%; height: 100%; }
  .photo--1 { left: 20px; }
  .photo--1 .photo__fill { background: linear-gradient(90deg, #e8e2dc 0%, #cdb6a6 40%, #b99a86 70%, #6d6a4a 100%); }
  .photo--2 { left: 238px; }
  .photo--2 .photo__fill { background: linear-gradient(90deg, #e9e9e6 0%, #a88c66 40%, #8a6b4a 55%, #c7bca9 100%); }
  .photo--3 { left: 456px; }
  .photo--3 .photo__fill { background: linear-gradient(90deg, #ece9e5 0%, #c9c0ae 40%, #b3a58e 70%, #7a5b45 100%); }
  .info-panel {
    position: absolute;
    left: 20px; right: 20px; top: 230px; bottom: 20px;
    background: var(--panel);
    border: 3px solid var(--frame);
    outline: 1px solid rgba(120,100,100,0.25);
    outline-offset: -8px;
    text-align: center;
  }
  .info-panel__perks {
    margin-top: 16px;
    font-size: 20px;
    line-height: 25px;
  }
  .sep { color: var(--accent); }
  .info-panel__call {
    margin-top: 15px;
    font-size: 26px;
    font-style: italic;
    color: var(--accent);
    letter-spacing: 0.5px;
  }
  .info-panel__services {
    margin-top: 10px;
    font-size: 18px;
  }
</style>
</head>
<body>

<section class="card card--front">
  <div class="sheer-backdrop" role="img" aria-label="Photo of sheer white curtains with a pink rose floral print"></div>
  <div class="inner-frame"></div>
  <div class="brand">
    <div class="brand__name"><span class="brand__dot"></span>Willow Lane Interiors</div>
    <p class="brand__tagline">Interiors that reflect your style</p>
  </div>
  <p class="slogan">Interiors that Reflect your Style!</p>
</section>

<section class="card card--back">
  <div class="sheer-backdrop" role="img" aria-label="Photo of sheer white curtains with a pink rose floral print"></div>
  <div class="photo photo--1"><div class="photo__fill" role="img" aria-label="Beige polka-dot curtain beside a sheer panel and a floor lamp"></div></div>
  <div class="photo photo--2"><div class="photo__fill" role="img" aria-label="Golden brown patterned curtain in a room with an armchair and painting"></div></div>
  <div class="photo photo--3"><div class="photo__fill" role="img" aria-label="Linen-coloured embroidered curtain beside a lamp and side table"></div></div>
  <div class="info-panel">
    <p class="info-panel__perks">free consultation on phone or in person<br>affordable prices <span class="sep">•</span> quality material guaranteed</p>
    <p class="info-panel__call">Call me: 202.555.0163</p>
    <p class="info-panel__services">blackout curtains <span class="sep">•</span> sheer curtains <span class="sep">•</span> valances <span class="sep">•</span> wall decorations</p>
  </div>
</section>

</body>
</html>
```